Oregon Pawnbroker About Us Brochure

We need to make a front/back tri-fold "about us" informative brochure using the bullet points uploaded. Our association represents licensed pawnbrokers in the state of Oregon and this will be distributed to the entire legislative body in our state. I have attached our logo, but feel free to be creative with logo to enhance the overall appearance of the brochure.

Target Market(s)

Regulators and Politicians

Industry/Entity Type

Pawnbroker

Requirements
Must have
• Professional Appearance
Nice to have
• Graphics, color scheme

```html
<!DOCTYPE html>
<html lang="en">
<head>
<meta charset="utf-8">
<title>Oregon Pawn Lenders Council – About Brochure</title>
<link href="https://fonts.googleapis.com/css2?family=Saira+Semi+Condensed:wght@300;400&display=swap" rel="stylesheet">
<style>
  :root{
    --navy:#0c1f35;
    --orange:#f04e1c;
    --white:#ffffff;
    --blush:#e3b7a8;
    --grey-dark:#2b2b2b;
    --grey-mid:#7d7f82;
    --band:rgba(90,90,90,.72);
  }
  *{margin:0;padding:0;box-sizing:border-box}
  html,body{width:1200px;height:848px;overflow:hidden;background:#fff}
  body{font-family:"Saira Semi Condensed",sans-serif;font-weight:300}
  .spread{position:relative;width:1200px;height:848px;overflow:hidden}
  .panel{position:absolute;top:0;height:848px;width:400px;overflow:hidden}
  .panel--about{left:0}
  .panel--inner{left:400px}
  .panel--cover{left:800px}

  .photo{position:absolute;inset:0}
  .photo--office{background:linear-gradient(180deg,#b9bcc0 0%,#8e9398 35%,#6d7176 70%,#4f5357 100%)}
  .photo--tower{background:linear-gradient(160deg,#eaeaea 0%,#bfbfbf 25%,#6a6a6a 60%,#3a3a3a 100%)}
  .photo--tower-cover{background:linear-gradient(200deg,#151515 0%,#3d3d3d 35%,#8a8a8a 65%,#2a2a2a 100%)}

  .top-rule{position:absolute;top:0;left:0;width:100%;height:12px}
  .top-rule--navy{background:var(--navy)}
  .top-rule--orange{background:var(--orange)}

  .about-card{position:absolute;left:45px;top:130px;width:311px;height:588px;background:var(--navy)}
  .about-fold{position:absolute;left:0;top:0}
  .about-title{position:absolute;right:30px;top:56px;text-align:right;color:var(--white);line-height:1}
  .about-title__kicker{font-size:20px;letter-spacing:.5px;display:block;margin-bottom:8px}
  .about-title__line{font-size:35px;display:block;line-height:34px;color:var(--orange)}
  .about-title__line .plain{color:var(--white)}
  .rule{position:absolute;left:55px;width:198px;border-top:1px dashed}
  .rule--light{top:207px;border-color:#8a93a0}
  .rule--accent{top:432px;border-color:var(--orange)}
  .about-points{position:absolute;left:28px;top:230px;width:254px;color:var(--white);font-size:16.5px;line-height:20px;text-align:justify}
  .about-points p{margin-bottom:14px}
  .coin-icon{position:absolute;left:34px;top:460px}

  .url{position:absolute;bottom:38px;left:0;width:100%;text-align:center;font-size:12.5px}
  .url--light{color:var(--white)}
  .url--dark{color:var(--navy)}
  .url--accent{color:var(--orange)}

  .inner-name{position:absolute;left:0;width:100%;top:402px;text-align:center;font-size:17px;letter-spacing:1px;line-height:21px}
  .inner-name__top{color:var(--navy);display:block}
  .inner-name__bottom{color:var(--orange);display:block}

  .brand{position:absolute;left:150px;top:114px;width:100px;text-align:center}
  .brand__dot{width:40px;height:40px;border-radius:50%;background:var(--white);margin:0 auto 8px}
  .brand__name{color:var(--white);font-size:12px;letter-spacing:1px;line-height:14px;font-weight:400}

  .cover-band{position:absolute;left:0;top:476px;width:400px;height:153px;background:var(--band)}
  .cover-title{position:absolute;left:80px;top:494px;font-size:40px;line-height:38px;letter-spacing:.5px}
  .cover-title span{display:block}
  .cover-title__a{color:var(--orange)}
  .cover-title__b{color:var(--white)}
  .cover-title__c{color:var(--navy)}
</style>
</head>
<body>
<main class="spread">

  <section class="panel panel--about">
    <div class="photo photo--office" role="img" aria-label="Black and white photo of a modern office interior with exposed ceiling ducts"></div>
    <div class="top-rule top-rule--navy"></div>
    <div class="about-card">
      <svg class="about-fold" width="130" height="40" viewBox="0 0 130 40" aria-hidden="true">
        <polygon points="0,22 125,0 80,37" fill="#fff"/>
      </svg>
      <h1 class="about-title">
        <span class="about-title__kicker">ABOUT</span>
        <span class="about-title__line"><span class="plain">THE</span> OREGON</span>
        <span class="about-title__line">PAWN LENDERS</span>
        <span class="about-title__line">COUNCIL</span>
      </h1>
      <div class="rule rule--light"></div>
      <div class="about-points">
        <p>United voice of Oregon Pawnbrokers</p>
        <p>Represents majority of pawnbrokers, both number of licensees and transactions processed</p>
        <p>Single point of contact for Oregon Legislature and all regulators to communicate with our industry.</p>
      </div>
      <div class="rule rule--accent"></div>
      <svg class="coin-icon" width="36" height="34" viewBox="0 0 36 34" aria-hidden="true">
        <circle cx="22" cy="12" r="10" fill="none" stroke="#f04e1c" stroke-width="1.6"/>
        <circle cx="14" cy="20" r="11" fill="#0c1f35" stroke="#f04e1c" stroke-width="1.6"/>
        <text x="14" y="25" text-anchor="middle" font-size="13" fill="#f04e1c" font-family="Saira Semi Condensed, sans-serif">$</text>
      </svg>
    </div>
    <p class="url url--light">www.oregonpawnlenderscouncil.org</p>
  </section>

  <section class="panel panel--inner">
    <div class="photo photo--tower" role="img" aria-label="Upward view of a glass skyscraper under a blush pink overlay"></div>
    <svg width="400" height="848" viewBox="0 0 400 848" style="position:absolute;inset:0" aria-hidden="true">
      <polygon points="0,340 260,130 400,470 400,848 0,848" fill="#e3b7a8" opacity=".92"/>
    </svg>
    <div class="top-rule top-rule--orange"></div>
    <p class="inner-name">
      <span class="inner-name__top">OREGON PAWN LENDERS</span>
      <span class="inner-name__bottom">COUNCIL</span>
    </p>
    <p class="url url--dark">www.oregonpawnlenderscouncil.org</p>
  </section>

  <section class="panel panel--cover">
    <div class="photo photo--tower-cover" role="img" aria-label="Dramatic black and white upward view of a skyscraper facade"></div>
    <div class="top-rule top-rule--orange"></div>
    <div class="brand">
      <div class="brand__dot"></div>
      <p class="brand__name">OREGON PAWN LENDERS COUNCIL</p>
    </div>
    <div class="cover-band"></div>
    <h2 class="cover-title">
      <span class="cover-title__a">OREGON</span>
      <span class="cover-title__b">PAWN LENDERS</span>
      <span class="cover-title__c">COUNCIL</span>
    </h2>
    <p class="url url--accent">www.oregonpawnlenderscouncil.org</p>
  </section>

</main>
</body>
</html>
```